Wordpress Web Design & Coding for velnoragroup.ca

We need a website for a new investment company that is visually grabbing and vibrant. We would like to see a web page that displays trust, growth and confidence. Needs to be responsive and mobile friendly for all browsers and coded for both Android & IOS.

Open to the number of pages and menu items. I selected 4 but if you feel the layout would work better with less I am open to this. Need to sell the people (management team/related businesses) and then show where the invested money will be going (upcoming projects).

Company Info:

Velnora is an investment company put together by a group of seasoned business professionals who have come together to combine decades of success in the real estate development, management, financing and medical services. The company will be a full service company offering turn key solutions for medical professionals.

Vel-Nora will focus on providing a full range of services via a group of distinct companies to deliver newly emerging needs of the medical community. The end goal will be to create complete solutions for individuals in the medical community. Our group has experience and success with the conceptualization, construction and financing of medical and dental clinic spaces. Vel-Nora Group will be established to accommodate all areas of the development and creation of clinics for medical professionals from building construction to equipment financing and administrations.

You can mention these companies and take photos from their websites. You can also use stock photos.

Our construction partner:
https://382bld.com/projects/

Our equipment leasing partner:
https://www.pordiva.com/

Our Management Team and medical partners

Gil Parkes
https://www.mysoundpoise.ca/

Milos Vendraker
https://www.qrtdentalservices.com/about-us

PROPOSED PROJECTS (see attachment for details)
Hollowmere Business Park
Cresfield Business Park
Mt. Corwin Ridge Professional

Investors

Investment

Sans Serif

Must have
• Wordpress – must be both desktop and mobile friendly with fast page load speed
Ability to edit after ourselves in Wordpress
Attractive home page with logo etc.
Logo colours are: for the blue the pantone color is #0355a3
and for the green is #8cc63f

Sections, about us, what we do/services we provide, contact us

```html
<!DOCTYPE html>
<html lang="en">
<head>
<meta charset="utf-8">
<title>Vel-Nora Group</title>
<link href="https://fonts.googleapis.com/css2?family=Roboto:wght@300;400;500;700;900&display=swap" rel="stylesheet">
<style>
:root{
  --brand-blue:#0355a3;
  --vivid-blue:#2b3cf2;
  --deep-blue:#1a12b4;
  --title-blue:#1b3fe0;
  --lime:#7ee93a;
  --lime-dark:#5fd92a;
  --green-text:#7ddc1f;
  --text-grey:#6b6f76;
  --ink:#1b1d22;
  --white:#ffffff;
  --orange:#f07a3c;
}
*{box-sizing:border-box;margin:0;padding:0}
html,body{width:1200px;height:3624px;overflow:hidden;background:#fafafa}
body{position:relative;font-family:'Roboto',Arial,sans-serif;color:var(--ink)}
.abs{position:absolute}
.fill{display:block}

/* brand */
.brand{left:0;top:40px;width:435px;display:flex;justify-content:center;align-items:center;gap:12px}
.brand-mark{width:28px;height:28px;background:var(--brand-blue)}
.brand-name{font-size:36px;font-weight:700;color:var(--brand-blue);letter-spacing:1px}
.menu-toggle{left:197px;top:226px;width:44px}
.menu-toggle span{display:block;height:3px;background:var(--orange);margin-bottom:11px}

/* hero */
.hero{left:0;top:293px;width:435px;height:256px;background:linear-gradient(160deg,#4d5357,#2d3236 60%,#3d4246);color:var(--white);text-align:center;padding-top:12px}
.hero h1{font-size:25px;font-weight:700;line-height:27px}
.hero h1 .accent{color:var(--lime)}
.hero p{font-size:14px;line-height:21px;padding:4px 10px 0;font-weight:400}
.hero-wave{left:0;top:505px;width:435px;height:60px}

/* about */
.about-title{left:0;top:566px;width:435px;text-align:center;font-size:52px;font-weight:700;color:var(--green-text)}
.about-text{left:6px;width:420px;text-align:center;font-size:13px;line-height:36px;color:var(--text-grey);font-weight:300}

/* partner cards */
.partner-photo{border:0}
.partner-card{background:var(--white);box-shadow:0 2px 8px rgba(0,0,0,.15);padding:10px 10px}
.partner-card h3{font-size:18px;font-weight:500;line-height:19px;margin-bottom:8px}
.partner-card p{font-size:7px;line-height:10px;color:#777}
.partner-logo{position:absolute;bottom:12px;left:0;right:0;text-align:center;font-size:12px;font-weight:700;color:var(--title-blue)}
.divider{left:70px;top:1484px;width:222px;height:2px;background:#e4e4e4}

/* management */
.team{left:0;top:1887px;width:435px;height:1070px;background:linear-gradient(135deg,#7ef03f,#62dc2e 50%,#8af04a)}
.team-title{left:0;top:1903px;width:435px;text-align:center;font-size:30px;font-weight:700;line-height:31px;color:var(--title-blue)}
.member-name{left:160px;font-size:27px;font-weight:500;color:var(--title-blue)}
.avatar{width:130px;height:130px;border-radius:50%;border:3px solid #2e3340}
.member-bio{left:165px;width:250px;font-size:21px;line-height:30px;color:var(--title-blue);letter-spacing:.3px}
.btn-blue{left:253px;width:158px;height:48px;background:#1833f0;color:var(--white);font-size:18px;font-weight:500;display:flex;align-items:center;justify-content:center}

/* leasing */
.leasing{left:11px;top:3004px;width:413px;height:509px;background:var(--vivid-blue);color:var(--white);padding:14px 12px}
.leasing h2{font-size:54px;line-height:54px;font-weight:700;letter-spacing:-.5px}
.leasing p{margin-top:22px;font-size:12px;line-height:17px;letter-spacing:-.2px}

/* security */
.security{left:777px;top:14px;width:409px;height:711px;background:var(--vivid-blue);color:var(--white);padding:6px 10px}
.security h2{font-size:53px;font-weight:700;line-height:64px}
.security p,.security li{font-size:18px;line-height:21.3px;letter-spacing:-.3px}
.security ul{padding-left:27px}

/* contracts */
.contracts{left:765px;top:868px;width:435px;height:1925px;background:linear-gradient(180deg,#cfe3f6,#bcd6ef 40%,#a9c7e7 70%,#c6dcf1)}
.contracts-title{left:765px;top:876px;width:435px;text-align:center;font-size:54px;font-weight:700;color:var(--title-blue)}
.project{background:#fafafa;box-shadow:0 2px 10px rgba(0,0,0,.18)}
.project h3{position:absolute;font-size:20px;font-weight:500}
.project p{position:absolute;font-size:12.5px;color:#777}
.btn-green{position:absolute;width:154px;height:48px;background:var(--lime);color:var(--white);font-size:18px;font-weight:500;display:flex;align-items:center;justify-content:center}

/* footer */
.footer{left:765px;top:2793px;width:435px;height:795px;background:var(--deep-blue);color:var(--white)}
.footer h4{position:absolute;left:23px;font-size:29px;font-weight:700}
.footer ul{position:absolute;left:53px;top:92px;font-size:20px;line-height:35.5px}
.footer .center{position:absolute;left:0;width:435px;text-align:center}
.icon-ring{width:38px;height:38px}
</style>
</head>
<body>

<!-- brand header -->
<div class="abs brand"><div class="brand-mark"></div><div class="brand-name">Vel-Nora Group</div></div>
<div class="abs menu-toggle"><span></span><span></span><span></span></div>

<!-- hero -->
<section class="abs hero" role="img" aria-label="Photo of a smiling professional in an office, dark overlay">
  <h1>Canada's<br><span class="accent">Fastest Growing Investment</span><br>Company!</h1>
  <p>Velnora is an investment company put together by a group of seasoned business professionals who have come together to combine decades of success in the real estate development, management, financing and medical services.</p>
</section>
<svg class="abs hero-wave" viewBox="0 0 435 60" preserveAspectRatio="none"><path d="M0 30 C60 0 120 40 200 30 S340 5 435 25 L435 60 L0 60Z" fill="#fafafa"/><path d="M0 30 C60 0 120 40 200 30 S340 5 435 25" fill="none" stroke="#2d3236" stroke-width="3"/></svg>

<!-- about -->
<h2 class="abs about-title">About Us</h2>
<p class="abs about-text" style="top:646px">We are a group of seasoned business professionals who have come together to combine decades of success in the real estate development, management, financing and medical services industries. This wide foundation of experience built on prior success, will used to strengthen existing industry partnerships.As well, new relationships will be developed to augment the existing group's strengths. The ultimate goal will be to enhance individual earnings and equity growth for our investors.</p>
<p class="abs about-text" style="top:946px">As we embark on this newest chapter, our combined knowledge will build on the discussions of the privatization in medical services that are ongoing at this time. One of our strategic goals to assist the medical community in catering to those services.</p>

<!-- construction partner -->
<div class="abs fill partner-photo" style="left:46px;top:1104px;width:276px;height:147px;background:linear-gradient(180deg,#7fb0e0,#bcd3e8 60%,#6e8a6a)" role="img" aria-label="Rendering of a modern office building"></div>
<div class="abs partner-card" style="left:70px;top:1235px;width:218px;height:226px">
  <h3>Construction Partner</h3>
  <p>382 Build Inc. is an established land developer and construction management company based in the prairies. Our projects are found across the region in many parks and range from design build of commercial office and warehouse space to interior improvements. Today, with a highly experienced team, 382 Build continues to design and build some of the most sought after commercial space on the market.</p>
  <div class="partner-logo">382 BUILD INC.</div>
</div>
<div class="abs divider"></div>

<!-- equipment partner -->
<div class="abs fill" style="left:44px;top:1491px;width:278px;height:158px;background:linear-gradient(180deg,#e9a23f,#c8702c 60%,#4a2e1c)" role="img" aria-label="Workers on a construction site at sunset"></div>
<div class="abs partner-card" style="left:68px;top:1611px;width:232px;height:242px">
  <h3>Equipment Leasing<br>Partner</h3>
  <p>At Pordiva Equipment Leasing, we specialize in putting together customized equipment leasing solutions that will keep your business moving forward. We know that obtaining traditional financing can be a difficult and time-consuming process, particularly if you are a new business or your business doesn't seem to fit in the box that traditional lenders use to define companies. Pordiva's small business focus and personalized service means fast approval and quick turnaround for your company's financing.</p>
  <div class="partner-logo" style="color:#8a6a2a;font-weight:400">PORDIVA</div>
</div>

<!-- management -->
<section class="abs team" role="img" aria-label="Green background with soft abstract texture"></section>
<h2 class="abs team-title">Our Management Team and<br>medical partners</h2>

<div class="abs member-name" style="top:1980px">Dr. Gil Parkes</div>
<div class="abs avatar" style="left:24px;top:2026px;background:radial-gradient(circle,#8a8f98,#3c4048)" role="img" aria-label="Portrait of Dr. Gil Parkes"></div>
<p class="abs member-bio" style="top:2026px">A published author and experienced, board-certified physician in the field of Bio-identical Hormone Replacement Therapy, Dr. Parkes believes in a holistic approach to helping men and women look stunning and feel great.</p>
<div class="abs btn-blue" style="top:2348px">Know More</div>

<div class="abs member-name" style="top:2437px">Dr. Gil Parkes</div>
<div class="abs avatar" style="left:24px;top:2484px;background:radial-gradient(circle,#9bb3c8,#3c4a58)" role="img" aria-label="Portrait of Milos Vendraker"></div>
<p class="abs member-bio" style="top:2485px">Milos brings over 25 years of experience in partnering with dentists across Western Canada as a dental consultant.He has been involved in building hundreds of clinics and has assisted clients with clinic location.</p>
<div class="abs btn-blue" style="top:2808px">Know More</div>

<!-- leasing operations -->
<section class="abs leasing">
  <h2>Leasing<br>Operations</h2>
  <p>The leasing division will allow investors to take advantage of a leverage portfolio and earn a net return on the investment that far exceeds conventional investment instruments available through commercial banks or other investment avenues. A blended repayment of interest and principal will be returned to the participants. As the fund grows and demand increases from medical and dental professionals seeking equipment, the portfolio will expand through bank participation. The management team will look to build on existing key relationship with institutions such as Norvale Bank, Tessic Credit and others, to establish a lower capital cost credit facility. The net proceeds between the interest on leases and bank credit facility will enhance earnings within the leasing company allowing for distribution to investors.</p>
</section>
<div class="abs fill" style="left:113px;top:3427px;width:282px;height:186px;background:linear-gradient(180deg,#b9c4cf,#8f9aa6 55%,#5c6570)" role="img" aria-label="Modern apartment living room with city view"></div>

<!-- security -->
<section class="abs security">
  <h2>Security</h2>
  <p>Vel-Nora Group leasing division will implement a number of security measures which ensures investors are secure and returns are maximized over the life of the investments.</p>
  <ul>
    <li>Bill of sale on the assets will be signed over from the originating Company to Vel-Nora Group.</li>
    <li>The lease agreements will be established with companies that are acquiring revenue generating assets. No personal leases are to be extended at the current time.</li>
    <li>Leases are co-signed by the owners of the comapnies acquring the asset.</li>
    <li>All leases have a registered General Secrity Agreement.</li>
    <li>The lease portfolio acquired by Vel-Nora will have an ages payment history dekonstraded by the lessee, rather than brand new leases.</li>
    <li>Payments collected via pre-authorized debits from lessees will be credited into a lock box bank account for distribution.</li>
    <li>Average outstanding lease amounts will be for less than $100k allowing for diversification.</li>
  </ul>
</section>
<div class="abs fill" style="left:796px;top:619px;width:352px;height:197px;background:radial-gradient(circle at 50% 45%,#2aa8a0,#0f3a55 45%,#071626)" role="img" aria-label="Businessman holding a tablet with a glowing padlock"></div>

<!-- contracts -->
<section class="abs contracts" role="img" aria-label="Faded city skyline background"></section>
<h2 class="abs contracts-title">Contracts...</h2>

<div class="abs project" style="left:822px;top:1003px;width:321px;height:434px">
  <div class="abs" style="left:39px;top:73px;width:242px;height:88px;background:linear-gradient(180deg,#e9eef2,#5b5f63 55%,#7f9a5a)" role="img" aria-label="Rendering of a business park building"></div>
  <h3 style="left:38px;top:182px">Cresfield Business Park</h3>
  <p style="left:38px;top:218px;width:250px;font-size:11.5px;line-height:24px">The city of Cresfield is a core municipality in the western Communities. It is currently experiencing regional increase in population driven by residential, commercial and industrial development.</p>
  <div class="btn-green" style="left:83px;top:346px">Read More</div>
</div>

<div class="abs project" style="left:820px;top:1559px;width:325px;height:598px">
  <div class="abs" style="left:51px;top:41px;width:225px;height:149px;background:linear-gradient(180deg,#cfd3d4,#8b8f8f 60%,#b49a78)" role="img" aria-label="Interior of a professional office lobby"></div>
  <h3 style="left:49px;top:210px;font-size:18px">Mt. Corwin Ridge Professional</h3>
  <p style="left:49px;top:254px;width:250px;line-height:33px">Mt. Corwin Professional building will feature a repurposed building adjacent to Corwin Ridge Road in Mt. Corwin, AB. This location served as a car dealership, but will be renovated from its current structure to a two storey building to</p>
  <div class="btn-green" style="left:87px;top:502px">Read more</div>
</div>

<div class="abs project" style="left:840px;top:2223px;width:328px;height:560px">
  <div class="abs" style="left:10px;top:77px;width:269px;height:151px;background:linear-gradient(180deg,#9fc1e0,#c9c6b8 50%,#6b7a58)" role="img" aria-label="Rendering of a mixed-use business park plaza"></div>
  <h3 style="left:10px;top:250px;font-size:22px">Hollowmere Business Park</h3>
  <p style="left:10px;top:296px;width:290px;font-size:15px;line-height:21.5px;color:#666">The Hollowmere Business Park in Cresfield, British Columbia on Vancouver Island, is presently under contract with partners that are controlled by individuals who form part of the Vel-Nora mangement group.</p>
  <div class="btn-green" style="left:67px;top:464px">Read more</div>
</div>

<!-- footer -->
<footer class="abs footer">
  <h4 style="top:16px">Useful Links</h4>
  <ul>
    <li>Home</li><li>About us</li><li>Services we provide</li><li>Contact us</li><li>Our Partners</li><li>Contracts</li>
  </ul>
  <h4 style="top:312px">Contact Information</h4>
  <div class="center" style="top:385px"><svg class="icon-ring" viewBox="0 0 38 38"><circle cx="19" cy="19" r="16" fill="none" stroke="#fff" stroke-width="1.5"/><path d="M19 10a6 6 0 0 0-6 6c0 5 6 12 6 12s6-7 6-12a6 6 0 0 0-6-6z" fill="none" stroke="#fff" stroke-width="1.8"/><circle cx="19" cy="16" r="2" fill="#fff"/></svg></div>
  <div class="center" style="top:438px;font-size:20px;line-height:35px">Lorem ipsum dolor sit amet, consectetur<br>adipiscing elit. Ut elit</div>
  <div class="center" style="top:513px"><svg class="icon-ring" viewBox="0 0 38 38"><circle cx="19" cy="19" r="16" fill="none" stroke="#fff" stroke-width="1.5"/><path d="M13 11l4 0 2 5-2.5 1.5a10 10 0 0 0 5 5L23 20l5 2v4c-9 1-16-6-15-15z" fill="none" stroke="#fff" stroke-width="1.8"/></svg></div>
  <div class="center" style="top:580px;font-size:22px;font-weight:700">+1 888 8888 88</div>
  <div class="center" style="top:647px"><svg class="icon-ring" viewBox="0 0 38 38"><circle cx="19" cy="19" r="16" fill="none" stroke="#fff" stroke-width="1.5"/><rect x="10" y="12" width="18" height="13" fill="none" stroke="#fff" stroke-width="1.8"/><path d="M10 12l9 8 9-8" fill="none" stroke="#fff" stroke-width="1.8"/></svg></div>
  <div class="center" style="top:727px;font-size:18px;font-weight:700">Email: info@velnoragroup.ca</div>
</footer>

</body>
</html>
```